Electrical Company Pickup Wrap

We are looking to have a wrap designed created for one of our newer pickup trucks that resembles our old truck letter design but has a little more flare.

Attached below are pictures of our existing trucks and logo file. The goal is to create a design that both incorporates much of our existing image but with a little flare.

The truck model for which we are looking for the wrap is a:
2021 Harlund Pexor TwinCab (4 door) See Picture Below

```html
<!DOCTYPE html>
<html lang="en">
<head>
<meta charset="utf-8">
<title>Kavo Electric LLC – Harlund Pexor TwinCab Wrap Layout</title>
<link rel="stylesheet" href="https://fonts.googleapis.com/css2?family=Audiowide&family=Michroma&display=swap">
<style>
  :root{
    --bg:#eef0f3;
    --wrap-white:#ffffff;
    --band-yellow:#f2c41c;
    --band-amber:#efae0f;
    --ink:#1b1b1b;
    --steel:#6d6f73;
    --olive:#b3a52a;
    --svc-blue:#2aa6d6;
    --svc-red:#b3192c;
    --svc-green:#3f9a3a;
    --edge:#d3d6db;
  }
  *{box-sizing:border-box;margin:0;padding:0}
  html,body{width:1200px;height:1200px;overflow:hidden;background:var(--bg)}
  body{position:relative;font-family:"Michroma",sans-serif;color:var(--ink)}

  .panel{position:absolute;background:var(--wrap-white);border:1px solid var(--edge);border-radius:18px;overflow:hidden}
  .side-panel{left:40px;top:70px;width:1120px;height:380px}
  .rear-panel{left:200px;top:540px;width:800px;height:330px}

  .band{position:absolute;left:0;width:100%}
  .side-panel .band{top:130px;height:76px;background:var(--band-yellow)}
  .rear-panel .band{top:124px;height:78px;background:var(--band-amber)}

  .brand{position:absolute;display:flex;align-items:center;gap:14px}
  .brand-mark{display:flex;align-items:center;gap:8px;font-family:"Audiowide",sans-serif;color:var(--ink)}
  .brand-mark .square{display:block;background:var(--ink)}
  .brand-divider{width:2px;background:var(--ink);align-self:stretch}
  .brand-name{font-family:"Audiowide",sans-serif;line-height:1;white-space:nowrap}
  .brand-name .accent{color:var(--wrap-white)}
  .brand-tag{font-family:"Michroma",sans-serif;white-space:nowrap;line-height:1}

  .side-panel .brand{left:340px;top:140px;height:56px}
  .side-panel .brand-mark{font-size:24px}
  .side-panel .brand-mark .square{width:15px;height:15px}
  .side-panel .brand-name{font-size:29px}
  .side-panel .brand-tag{font-size:11px;letter-spacing:6.4px;margin-top:8px}

  .rear-panel .brand{left:22px;top:222px;height:76px}
  .rear-panel .brand-mark{font-size:32px}
  .rear-panel .brand-mark .square{width:22px;height:22px}
  .rear-panel .brand-name{font-size:36px}
  .rear-panel .brand-name .accent{color:var(--olive)}
  .rear-panel .brand-tag{font-size:12px;letter-spacing:8px;margin-top:10px}

  .service{position:absolute;display:flex;align-items:center;gap:8px}
  .service .svc-mark{display:flex;align-items:center;gap:5px;font-family:"Audiowide",sans-serif;font-size:15px}
  .service .svc-mark i{display:block;width:10px;height:10px}
  .service .svc-divider{width:1.5px;height:28px;background:var(--ink)}
  .service .svc-label{font-size:10px;line-height:1.4;letter-spacing:.4px;white-space:nowrap}
  .svc-automation i{background:var(--svc-blue)}
  .svc-fire i{background:var(--svc-red)}
  .svc-data i{background:var(--svc-green)}

  .side-panel .svc-automation{left:340px;top:232px}
  .side-panel .svc-fire{left:660px;top:232px}
  .side-panel .svc-data{left:340px;top:290px}

  .rear-panel .svc-automation{left:22px;top:20px}
  .rear-panel .svc-fire{left:22px;top:70px}
  .rear-panel .svc-data{right:22px;top:28px}

  .phone{position:absolute;font-family:"Audiowide",sans-serif;white-space:nowrap}
  .side-panel .phone{right:64px;top:66px;font-size:34px;color:var(--steel)}
  .rear-panel .band-text{position:absolute;top:50%;transform:translateY(-50%);font-family:"Audiowide",sans-serif;font-size:18px;color:var(--ink);white-space:nowrap}
  .rear-panel .website{left:22px}
  .rear-panel .band .phone{right:22px;font-size:21px;top:50%;transform:translateY(-50%)}
  .maker-name{position:absolute;left:50%;top:50%;transform:translate(-50%,-50%);font-family:"Michroma",sans-serif;font-size:12px;color:var(--ink);letter-spacing:1px}
</style>
</head>
<body>
  <section class="panel side-panel" aria-label="Side wrap layout">
    <div class="band"></div>
    <div class="phone">555-018-4470</div>

    <div class="brand">
      <div class="brand-mark"><span class="square"></span>KAVO</div>
      <span class="brand-divider"></span>
      <div>
        <div class="brand-name">KAVO <span class="accent">ELECTRIC</span> LLC</div>
        <div class="brand-tag">ELECTRICAL CONTRACTORS</div>
      </div>
    </div>

    <div class="service svc-automation">
      <div class="svc-mark"><i></i>KAVO</div><span class="svc-divider"></span>
      <div class="svc-label">BUILDING AUTOMATION<br>&amp; CONTROLS</div>
    </div>
    <div class="service svc-fire">
      <div class="svc-mark"><i></i>KAVO</div><span class="svc-divider"></span>
      <div class="svc-label">FIRE, SECURITY<br>&amp; ACCESS CONTROL</div>
    </div>
    <div class="service svc-data">
      <div class="svc-mark"><i></i>KAVO</div><span class="svc-divider"></span>
      <div class="svc-label">DATA/<br>TELECOMMUNICATIONS</div>
    </div>
  </section>

  <section class="panel rear-panel" aria-label="Tailgate wrap layout">
    <div class="service svc-automation">
      <div class="svc-mark"><i></i>KAVO</div><span class="svc-divider"></span>
      <div class="svc-label">BUILDING AUTOMATION<br>&amp; CONTROLS</div>
    </div>
    <div class="service svc-fire">
      <div class="svc-mark"><i></i>KAVO</div><span class="svc-divider"></span>
      <div class="svc-label">FIRE, SECURITY<br>&amp; ACCESS CONTROL</div>
    </div>
    <div class="service svc-data">
      <div class="svc-mark"><i></i>KAVO</div><span class="svc-divider"></span>
      <div class="svc-label">DATA/<br>TELECOMMUNICATIONS</div>
    </div>

    <div class="band">
      <span class="band-text website">KAVOELECTRIC.COM</span>
      <span class="maker-name">HARLUND</span>
      <span class="phone">555-018-4470</span>
    </div>

    <div class="brand">
      <div class="brand-mark"><span class="square"></span>KAVO</div>
      <span class="brand-divider"></span>
      <div>
        <div class="brand-name">KAVO <span class="accent">ELECTRIC</span> LLC</div>
        <div class="brand-tag">ELECTRICAL CONTRACTORS</div>
      </div>
    </div>
  </section>
</body>
</html>
```